Web design and optimisation

We are merging with another company. We require the following pages to be incorporated into our website but with a consistent look and feel and a general tidy up of our entire website. It needs to be optimised for web and mobile viewing and we want more hits on the site.

Our existing site needs some tidying up. We like a fresh, clean, contemporary and professional look.

Our current site:
harbourline checks.com.au
The site that needs to be merged is sunridgepropertyandpest.com.au
We only need the pages that relate to the "termite services" and and "pest control"

```html
<!DOCTYPE html>
<html lang="en">
<head>
<meta charset="utf-8">
<title>Harbourline Checks</title>
<link href="https://fonts.googleapis.com/css2?family=Rajdhani:wght@600;700&family=Poppins:ital,wght@0,400;0,500;0,600;1,400&display=swap" rel="stylesheet">
<style>
:root{
  --blue:#1b8fd2;
  --blue-dark:#1670b8;
  --teal:#15a996;
  --ink:#343a40;
  --body:#4a4f55;
  --pale:#e3eef8;
  --card-bg:#f3f9f8;
  --grey:#c9cdd1;
}
*{box-sizing:border-box;margin:0;padding:0}
html,body{width:1200px;height:4751px;overflow:hidden}
body{position:relative;font-family:'Poppins',sans-serif;color:var(--body);background:#fff}
.abs{position:absolute}
.heading{font-family:'Rajdhani',sans-serif;font-weight:700;text-transform:uppercase;color:var(--ink);letter-spacing:.5px}
.btn{position:absolute;display:flex;align-items:center;justify-content:center;font-family:'Rajdhani',sans-serif;font-weight:700;text-transform:uppercase;color:#fff;font-size:16px;letter-spacing:.5px}
.btn-blue{background:var(--blue)}
.btn-teal{background:var(--teal)}
.rule{position:absolute;height:3px;width:70px;background:var(--blue)}
.rule::after{content:"";position:absolute;left:10px;top:8px;width:50px;height:3px;background:var(--teal)}

/* header */
.topnav{position:absolute;top:22px;left:397px;display:flex;gap:30px;font-size:13px;color:var(--blue);font-weight:500}
.topnav .call{font-weight:600;font-size:17px;margin-top:-3px}
.book-top{left:922px;top:0;width:148px;height:63px;font-size:17px}
.brand{position:absolute;left:130px;top:62px;font-size:30px;color:var(--blue-dark);font-weight:500;line-height:1}
.brand small{display:block;font-size:17px;color:var(--blue);letter-spacing:2px;text-align:right;margin-top:2px}
.mainnav{position:absolute;top:96px;left:400px;display:flex;gap:35px;font-size:14px;color:var(--blue);font-weight:500}

/* hero */
.hero{position:absolute;top:138px;left:0;width:1200px;height:630px;background:linear-gradient(100deg,#6d5a46 0%,#8a8d88 30%,#a6a8aa 60%,#d8dadb 100%)}
.hero-title{left:697px;top:262px;font-size:56px;line-height:.95;color:#fff}
.hero-text{left:697px;top:383px;width:330px;color:#fff;font-size:16px;line-height:1.5}
.hero-btn{left:700px;top:452px;width:140px;height:53px}
.hero-edge{position:absolute;left:0;top:660px}

/* services */
.sec-title{width:1200px;text-align:center;font-size:38px}
.block-title{font-size:31px;line-height:1;color:var(--blue)}
.block-title.teal{color:var(--teal)}
.block-text{font-size:12.4px;line-height:1.5}
.card{position:absolute;background:#fff;box-shadow:0 2px 8px rgba(0,0,0,.14);text-align:center}
.card .ph{height:170px}
.card h4{font-family:'Rajdhani',sans-serif;font-weight:700;text-transform:uppercase;font-size:16px;margin-top:22px;color:var(--blue)}
.card p{font-size:11.5px;line-height:1.35;margin:10px 24px 0}
.card.t h4{color:var(--teal)}
.dots{left:125px;top:1317px;width:948px;border-top:3px dotted var(--teal)}

/* why */
.why{position:absolute;top:1778px;left:0;width:1200px;height:631px;background:linear-gradient(160deg,#17ab93 0%,#1b9bc0 55%,#1b86cf 100%)}
.why h2{color:#fff;font-size:38px}
.why p{color:#fff;font-size:12.4px;line-height:1.5}
.ticks{list-style:none;color:#fff;font-size:19px;line-height:34px}
.ticks li{display:flex;align-items:center;gap:10px}
.ring{left:667px;top:1935px;width:388px;height:388px;border-radius:50%;background:#7ec9dd;border:4px solid #3fb0c8}
.ring div{position:absolute;inset:16px;border-radius:50%;background:linear-gradient(140deg,#4f7b35,#a35fa8 55,#b79fcf)}

/* program */
.prog-name{left:728px;top:2600px;width:270px;text-align:center;font-size:44px;font-weight:600;color:var(--teal)}

/* team */
.team-photo{left:0;top:2917px;width:725px;height:487px;background:linear-gradient(180deg,#6a4a38 0%,#4d3d36 40%,#2a3142 75%,#786a5c 100%)}
.team-panel{left:614px;top:2962px;width:586px;height:396px;background:var(--pale)}

/* reviews */
.quote{position:absolute;top:3642px;width:296px;height:280px;background:var(--card-bg);padding:30px 40px}
.quote .mark{font-family:'Rajdhani',sans-serif;font-size:48px;font-weight:700;color:var(--teal);line-height:.6;height:28px}
.quote p{font-style:italic;font-size:13.6px;line-height:1.45;margin-top:18px;color:#555}
.quote h5{font-family:'Rajdhani',sans-serif;font-weight:700;font-size:15px;color:var(--teal);margin-top:26px;text-transform:uppercase}
.partner{position:absolute;background:var(--grey);opacity:.75}

/* footer */
.footer{position:absolute;top:4257px;left:0;width:1200px;height:494px;background:linear-gradient(180deg,#15a996 0%,#1a9bc5 60%,#1b8fd2 100%)}
.field{position:absolute;background:#fff;font-size:14px;color:#444;padding:10px 12px}
.loc{color:#fff;font-size:12.5px;line-height:1.5}
.loc-row{position:absolute;left:579px;display:flex;gap:10px;color:#fff;font-size:12.5px;line-height:1.5}
.social{position:absolute;top:4622px;width:26px;height:26px;border-radius:50%;background:#fff}
.foot-brand{left:838px;top:4520px;color:#fff;font-size:42px;font-weight:500;line-height:1;text-align:right;width:228px}
.foot-brand small{display:block;font-size:24px;letter-spacing:2px}
</style>
</head>
<body>

<header>
  <nav class="topnav"><span>BUILDING REPORTS</span><span>EXPLORE</span><span>PRICING</span><span class="call">CALL:(02) 5550 1742</span></nav>
  <a class="btn btn-teal book-top">Book Now</a>
  <div class="brand">Harbourline<small>CHECKS</small></div>
  <nav class="mainnav"><span>HOME</span><span>TERMITE SERVICES</span><span>PEST CONTROL</span><span>ABOUT US</span><span>FAQ</span><span>CONTACT US</span></nav>
</header>

<section class="hero" role="img" aria-label="Photo of a technician spraying a skirting board while a homeowner watches"></section>
<h1 class="abs heading hero-title" style="color:#fff">Harbourline<br>Checks</h1>
<p class="abs hero-text">Lorem ipsum dolor sit amet, consectetur adipiscing elit, sed do eiusmod tempor</p>
<a class="btn btn-blue hero-btn">Book Now</a>
<svg class="hero-edge" width="1200" height="110" viewBox="0 0 1200 110">
  <path d="M0 110 L0 102 L598 26 L1200 102 L1200 110 Z" fill="#fff"/>
  <path d="M0 100 L598 18 L1200 100" fill="none" stroke="#1b8fd2" stroke-width="5"/>
  <path d="M300 72 L598 32 L1010 84" fill="none" stroke="#15a996" stroke-width="3"/>
</svg>

<h2 class="abs heading sec-title" style="top:800px">Our Services</h2>
<div class="rule" style="left:565px;top:857px"></div>

<h3 class="abs heading block-title" style="left:130px;top:938px">Termite<br>Services</h3>
<p class="abs block-text" style="left:130px;top:1020px;width:215px">Lorem ipsum dolor sit amlore et, consectetur adipiscing elit, sedo eiusmod tempor inci didunt lout labolore et dolore magna aliqua. Ut enim ad min im veniam, quis nostxercitation ullamco laoloris liuiponsequa is aute irure doin reprehenderit in voluptate.</p>
<a class="btn btn-blue" style="left:130px;top:1190px;width:112px;height:41px">View More</a>

<div class="card" style="left:380px;top:940px;width:217px;height:298px"><div class="ph" role="img" aria-label="Close-up photo of termites on soil" style="background:linear-gradient(135deg,#b59a78,#7e6648)"></div><h4>Termite Protection</h4><p>Lorem ipsum dolor sit ae consectetur adipiscing eli sed do eiusmod tem.</p></div>
<div class="card" style="left:616px;top:940px;width:217px;height:298px"><div class="ph" role="img" aria-label="Photo of a worker treating a garden lawn" style="background:linear-gradient(180deg,#8a8f7a,#5d9a3a)"></div><h4>Termite Treatments</h4><p>Lorem ipsum dolor sit ae consectetur adipiscing eli sed do eiusmod tem.</p></div>
<div class="card" style="left:852px;top:940px;width:215px;height:298px"><div class="ph" role="img" aria-label="Photo of an inspector in protective suit checking a storeroom" style="background:linear-gradient(135deg,#a88d6e,#d8d4cf)"></div><h4>Termite Inspections</h4><p>Lorem ipsum dolor sit ae consectetur adipiscing eli sed do eiusmod tem.</p></div>

<div class="abs dots"></div>

<div class="card t" style="left:130px;top:1384px;width:217px;height:297px"><div class="ph" role="img" aria-label="Photo of a technician in a white suit spraying indoors" style="background:linear-gradient(135deg,#6b5a4c,#c9c6c1)"></div><h4>Ant Control</h4><p>Lorem ipsum dolor sit ae consectetur adipiscing eli sed do eiusmod tem.</p></div>
<div class="card t" style="left:365px;top:1384px;width:217px;height:297px"><div class="ph" role="img" aria-label="Photo of a technician spraying a kitchen cabinet" style="background:linear-gradient(135deg,#5a4232,#e6e3df)"></div><h4>Cockroach Control</h4><p>Lorem ipsum dolor sit ae consectetur adipiscing eli sed do eiusmod tem.</p></div>
<div class="card t" style="left:601px;top:1384px;width:217px;height:297px"><div class="ph" role="img" aria-label="Photo of a worker spraying a lawn with a backpack sprayer" style="background:linear-gradient(180deg,#6a7b52,#4f8f35)"></div><h4>Spider Control</h4><p>Lorem ipsum dolor sit ae consectetur adipiscing eli sed do eiusmod tem.</p></div>

<h3 class="abs heading block-title teal" style="left:864px;top:1382px">Pest<br>Control</h3>
<p class="abs block-text" style="left:864px;top:1462px;width:210px">Lorem ipsum dolor sit amlore et, consectetur adipiscing elit, sedo eiusmod tempor inci didunt lout labolore et dolore magna aliqua. Ut enim ad min im veniam, quis nostxercitation ullamco laoloris liuiponsequa is aute irure doin reprehenderit in voluptate.</p>
<a class="btn btn-teal" style="left:864px;top:1634px;width:112px;height:41px">View More</a>

<section class="why">
  <svg class="abs" style="left:0;top:0" width="1200" height="80" viewBox="0 0 1200 80">
    <path d="M0 0 L1200 0 L1200 4 L600 58 L0 4 Z" fill="#fff"/>
    <path d="M0 10 L600 66 L1200 10" fill="none" stroke="#1b8fd2" stroke-width="5"/>
    <path d="M240 34 L600 60 L1000 28" fill="none" stroke="#ffffff" stroke-width="2" opacity=".7"/>
  </svg>
  <h2 class="abs heading" style="left:130px;top:186px">Why Choose Us?</h2>
  <div class="abs" style="left:130px;top:250px;width:80px;height:3px;background:#fff"></div>
  <div class="abs" style="left:140px;top:258px;width:60px;height:3px;background:#fff;opacity:.6"></div>
  <p class="abs" style="left:130px;top:283px;width:420px">Lorem ipsum dolor sit amlore et, consectetur adipiscing elit, sedo eiusmod tempor inci didunt lout labolore et dolore magna aliqua. Ut enim ad min im veniam, quis nostxercitation ullamco laoloris liuiponsequa is aute irure doin reprehenderit in</p>
  <ul class="abs ticks" style="left:130px;top:378px">
    <li><svg width="16" height="16" viewBox="0 0 16 16"><circle cx="8" cy="8" r="8" fill="#fff"/><path d="M4.5 8.2l2.3 2.3 4.7-4.7" fill="none" stroke="#1b9bc0" stroke-width="2"/></svg>We've been around the longest.</li>
    <li><svg width="16" height="16" viewBox="0 0 16 16"><circle cx="8" cy="8" r="8" fill="#fff"/><path d="M4.5 8.2l2.3 2.3 4.7-4.7" fill="none" stroke="#1b9bc0" stroke-width="2"/></svg>We've done more inspections.</li>
    <li><svg width="16" height="16" viewBox="0 0 16 16"><circle cx="8" cy="8" r="8" fill="#fff"/><path d="M4.5 8.2l2.3 2.3 4.7-4.7" fill="none" stroke="#1b9bc0" stroke-width="2"/></svg>Our turnaround and quality is unsurpassed.</li>
    <li><svg width="16" height="16" viewBox="0 0 16 16"><circle cx="8" cy="8" r="8" fill="#fff"/><path d="M4.5 8.2l2.3 2.3 4.7-4.7" fill="none" stroke="#1b9bc0" stroke-width="2"/></svg>Buyers want our reports.</li>
  </ul>
</section>
<div class="abs ring"><div role="img" aria-label="Photo of a worker in protective gear fogging garden shrubs"></div></div>

<h2 class="abs heading" style="left:138px;top:2518px;font-size:38px">Under One Sky</h2>
<p class="abs" style="left:138px;top:2611px;width:490px;font-size:13.6px;line-height:1.5">Every year we step into hundreds of homes across the city, yet in Canberra there are still so many people living without acceptable, permanent or safe shelter. Whilst we commit our resources to many charities throughout the year, our in-house program 'Under One Sky' focuses on supporting members of our community who do not have a place to call home.</p>
<a class="btn btn-blue" style="left:138px;top:2768px;width:148px;height:38px;font-size:14px;background:linear-gradient(90deg,#15a996,#1b8fd2)">Read More</a>
<div class="abs prog-name">Under One Sky</div>

<div class="abs team-photo" role="img" aria-label="Group photo of the company team seated and standing outdoors with a dog"></div>
<section class="abs team-panel">
  <h2 class="abs heading" style="left:49px;top:46px;font-size:38px">Who We Are</h2>
  <div class="rule" style="left:55px;top:111px"></div>
  <p class="abs" style="left:55px;top:148px;width:400px;font-size:13.6px;line-height:1.5">After the best part of two decades and 20,000 plus residential inspections… we live and breathe local property! From our grassroots family beginnings we have worked hard to shape Harbourline Checks into a dynamic, award winning, service-focused business proudly employing Canberra's best building inspection professionals who are supported by an outstanding administrative team managing customer service.</p>
  <a class="btn btn-blue" style="left:55px;top:319px;width:147px;height:37px;font-size:14px;background:linear-gradient(90deg,#15a996,#1b8fd2)">Meet Our Team</a>
</section>

<h2 class="abs heading sec-title" style="top:3535px">Our Customers Say</h2>
<div class="quote" style="left:129px"><div class="mark">“</div><p>I chose Harbourline Checks because of their local charity program, they were fast, professional and reasonably priced. I would not hesitate to recommend them to a friend and I will definitely be using them again next time.</p><h5>-Martin, Kingston</h5></div>
<div class="quote" style="left:452px"><div class="mark">“</div><p>I loved the fact that the inspector was right on time, and the report is very comprehensive. Your staff are courteous and helpful, great customer service from start to finish. I couldn't have asked for more!</p><h5>-Sandra, Florey</h5></div>
<div class="quote" style="left:772px"><div class="mark">“</div><p>Your inspector was customer focused, fair, honest and extremely professional in his approach. On the basis of my personal experience, I would highly recommend the inspector and the organisation he represents</p><h5>-Helen, Ainslie</h5></div>

<div class="partner" style="left:228px;top:4040px;width:124px;height:66px"></div>
<div class="partner" style="left:450px;top:4060px;width:126px;height:34px"></div>
<div class="partner" style="left:648px;top:4044px;width:184px;height:60px"></div>
<div class="partner" style="left:904px;top:4033px;width:122px;height:74px"></div>
<div class="partner" style="left:187px;top:4143px;width:160px;height:74px"></div>
<div class="partner" style="left:425px;top:4160px;width:153px;height:38px"></div>
<div class="partner" style="left:640px;top:4160px;width:190px;height:38px"></div>
<div class="partner" style="left:876px;top:4151px;width:186px;height:56px"></div>

<footer class="footer">
  <svg class="abs" style="left:0;top:0" width="1200" height="80" viewBox="0 0 1200 80">
    <path d="M0 0 L1200 0 L1200 4 L600 58 L0 4 Z" fill="#fff"/>
    <path d="M0 10 L600 66 L1200 10" fill="none" stroke="#1b8fd2" stroke-width="5"/>
    <path d="M240 34 L600 60 L1000 28" fill="none" stroke="#ffffff" stroke-width="2" opacity=".7"/>
  </svg>
  <h2 class="abs heading" style="left:129px;top:146px;font-size:38px;color:#fff">Contact Us</h2>
  <div class="field" style="left:129px;top:212px;width:195px;height:41px">Name</div>
  <div class="field" style="left:339px;top:212px;width:196px;height:41px">Phone</div>
  <div class="field" style="left:129px;top:264px;width:406px;height:41px">Email</div>
  <div class="field" style="left:129px;top:314px;width:406px;height:101px">Message</div>
  <a class="btn btn-teal" style="left:405px;top:389px;width:111px;height:30px">Submit</a>

  <h3 class="abs heading" style="left:579px;top:162px;font-size:20px;color:#fff">Location</h3>
  <div class="loc-row" style="top:198px"><svg width="12" height="16" viewBox="0 0 12 16"><path d="M6 0a6 6 0 0 0-6 6c0 4.5 6 10 6 10s6-5.5 6-10a6 6 0 0 0-6-6z" fill="#fff"/><circle cx="6" cy="6" r="2.2" fill="#1a9bc5"/></svg><span>Company name line56<br>lorem ipshm street 67 lore<br>slorhort 56747</span></div>
  <div class="loc-row" style="top:275px"><svg width="13" height="13" viewBox="0 0 24 24"><path d="M6.6 10.8a15 15 0 0 0 6.6 6.6l2.2-2.2c.3-.3.7-.4 1-.2 1.1.4 2.3.6 3.6.6.6 0 1 .4 1 1V20c0 .6-.4 1-1 1C10.6 21 3 13.4 3 4c0-.6.4-1 1-1h3.5c.6 0 1 .4 1 1 0 1.3.2 2.5.6 3.6.1.3 0 .7-.2 1z" fill="#fff"/></svg><span>Phone:02 5550 1743</span></div>
  <div class="loc-row" style="top:313px"><svg width="13" height="11" viewBox="0 0 13 11"><rect width="13" height="11" rx="1" fill="#fff"/><path d="M0.5 1l6 5 6-5" fill="none" stroke="#1b8fd2" stroke-width="1.2"/></svg><span>Email:info@harbourlinechecks.com.au</span></div>
  <span class="social" style="left:585px"></span>
  <span class="social" style="left:628px"></span>
  <span class="social" style="left:667px"></span>

  <div class="abs foot-brand" style="top:263px">Harbourline<small>CHECKS</small></div>
  <p class="abs" style="left:843px;top:370px;color:#fff;font-size:12.5px">Copyright © 2022 All Right Reserved</p>
</footer>

</body>
</html>
```